Home Baker of cakes, muffins, cookies and pastries.

I am looking for business cards for my home baking business called " Zippy Pom-Pom Bakes " - I want them to be super cute and girly, yet simple and modern at the same time. Pastel colours is what I envision with the main colour being baby pink.

```html
<!DOCTYPE html>
<html lang="en">
<head>
<meta charset="utf-8">
<title>Zippy Pom-Pom Bakes – Business Cards</title>
<link href="https://fonts.googleapis.com/css2?family=Great+Vibes&family=Lato:wght@400;700&display=swap" rel="stylesheet">
<style>
  :root {
    --backdrop: #2b2b2c;
    --baby-pink: #ec8aaa;
    --baby-pink-light: #f29bb7;
    --charcoal: #343434;
    --white: #ffffff;
    --mint: #86d3d8;
    --rose: #f08db0;
  }
  * { box-sizing: border-box; margin: 0; padding: 0; }
  html, body {
    width: 1200px; height: 900px; overflow: hidden;
    background: var(--backdrop);
    font-family: "Lato", sans-serif;
  }
  .canvas { position: relative; width: 1200px; height: 900px; }

  .card {
    position: absolute;
    width: 560px; height: 320px;
    border-radius: 16px;
    box-shadow: 0 18px 40px rgba(0,0,0,.45);
    overflow: hidden;
  }

  /* Pink contact card */
  .card--front {
    left: 90px; top: 90px;
    background: linear-gradient(135deg, var(--baby-pink) 0%, var(--baby-pink-light) 100%);
    color: var(--white);
  }
  .front-brand {
    position: absolute; left: 0; right: 0; top: 62px;
    text-align: center;
  }
  .brand-line {
    display: inline-flex; align-items: center; gap: 10px;
    font-weight: 700; font-size: 30px; letter-spacing: .5px;
  }
  .brand-dot {
    width: 16px; height: 16px; border-radius: 50%;
    background: currentColor;
  }
  .brand-rule {
    width: 320px; height: 2px; margin: 10px auto 8px;
    background: var(--white); opacity: .9;
  }
  .brand-tagline {
    font-size: 13px; letter-spacing: 8px; font-weight: 400;
  }
  .owner {
    position: absolute; right: 36px; top: 170px; text-align: right;
  }
  .owner-name { font-family: "Great Vibes", cursive; font-size: 30px; line-height: 1; }
  .owner-role { font-size: 11px; letter-spacing: .5px; margin-top: 2px; }

  .contact-list {
    position: absolute; left: 36px; bottom: 34px;
    list-style: none; font-size: 13px; line-height: 1.75;
  }
  .contact-list li { display: flex; align-items: center; gap: 10px; }
  .contact-list svg { width: 13px; height: 13px; fill: var(--white); flex: none; }

  /* Charcoal brand card */
  .card--back {
    left: 550px; top: 480px;
    background: var(--charcoal);
  }
  .back-brand {
    position: absolute; left: 0; right: 0; top: 92px; text-align: center;
  }
  .back-brand .rule-top {
    width: 420px; height: 3px; margin: 0 auto 18px;
    background: var(--mint); border-radius: 2px;
  }
  .back-brand .brand-line { color: var(--rose); font-size: 36px; }
  .back-brand .rule-bottom {
    width: 420px; height: 2px; margin: 16px auto 0;
    background: var(--mint);
  }
  .website {
    position: absolute; left: 0; right: 0; bottom: 58px;
    text-align: center; color: var(--rose);
    font-size: 14px; letter-spacing: 3px;
  }
</style>
</head>
<body>
<main class="canvas">

  <section class="card card--front" aria-label="Business card front">
    <div class="front-brand">
      <div class="brand-line"><span class="brand-dot"></span>Zippy Pom-Pom Bakes</div>
      <div class="brand-rule"></div>
      <div class="brand-tagline">HOME BAKERS</div>
    </div>

    <div class="owner">
      <div class="owner-name">Maribel Thornquist</div>
      <div class="owner-role">Owner / Founder</div>
    </div>

    <ul class="contact-list">
      <li>
        <svg viewBox="0 0 24 24" aria-hidden="true"><path d="M6.6 10.8a15 15 0 0 0 6.6 6.6l2.2-2.2a1 1 0 0 1 1-.25 11.4 11.4 0 0 0 3.6.57 1 1 0 0 1 1 1V20a1 1 0 0 1-1 1A17 17 0 0 1 3 4a1 1 0 0 1 1-1h3.5a1 1 0 0 1 1 1c0 1.25.2 2.45.57 3.6a1 1 0 0 1-.25 1z"/></svg>
        555.204.3318
      </li>
      <li>
        <svg viewBox="0 0 24 24" aria-hidden="true"><path d="M2 5h20v14H2zm2 2v.5l8 5 8-5V7l-8 5z"/></svg>
        mthornquist@zippypompom.com
      </li>
      <li>
        <svg viewBox="0 0 24 24" aria-hidden="true"><path d="M12 2a7 7 0 0 0-7 7c0 5 7 13 7 13s7-8 7-13a7 7 0 0 0-7-7zm0 9.5A2.5 2.5 0 1 1 12 6.5a2.5 2.5 0 0 1 0 5z"/></svg>
        742 Maple Crest Ln, Brookfield, OH - 44403
      </li>
    </ul>
  </section>

  <section class="card card--back" aria-label="Business card back">
    <div class="back-brand">
      <div class="rule-top"></div>
      <div class="brand-line"><span class="brand-dot"></span>Zippy Pom-Pom Bakes</div>
      <div class="rule-bottom"></div>
    </div>
    <div class="website">www.zippypompom.com</div>
  </section>

</main>
</body>
</html>
```